" A Virtal Soluçoes Ambientais é uma empresa que presta serviços de regularizaçao ambiental. Trata-se de uma consultoria ambiental cujo principal serviço é oferecer soluçoes ambientais para atividades produtivas e imóveis urbanos ou rurais. Exemplos: (i) correçao de matrículas e registros em órgao públicos para fazendas produtivas; (ii) correçao de emissoes atmosféricas, ruídos, resíduos, etc, de indústrias; (iii) descontaminaçao do solo ou água subterrânea de um imóvel; (iv) elaboraçao de laudos técnicos sobre passivos ambientais. Observaçao importante: a empresa nao é uma ONG, embora o apelo seja ambiental. "

```html
<!DOCTYPE html>
<html lang="pt-BR">
<head>
<meta charset="UTF-8">
<title>Virtal Soluçoes Ambientais — Envelopes</title>
<link rel="stylesheet" href="https://fonts.googleapis.com/css2?family=Josefin+Sans:wght@300;400&display=swap">
<style>
  :root {
    --page-bg: #e6e7e6;
    --teal-deep: #2f4b47;
    --teal-soft: #3b5954;
    --paper: #f7f7f6;
    --paper-shade: #e9eaea;
    --ink-muted: #7d8785;
    --gold-line: #b8a77a;
    --white: #ffffff;
  }
  * { box-sizing: border-box; margin: 0; padding: 0; }
  html, body {
    width: 1200px;
    height: 1200px;
    overflow: hidden;
    background: var(--page-bg);
    font-family: "Josefin Sans", sans-serif;
  }
  .stationery {
    position: relative;
    width: 1200px;
    height: 1200px;
  }

  /* Front envelope */
  .envelope-front {
    position: absolute;
    left: 250px;
    top: 230px;
    width: 370px;
    height: 680px;
    background: var(--teal-deep);
    overflow: hidden;
    box-shadow: 0 6px 18px rgba(0,0,0,0.18);
  }
  .envelope-front .globe-area {
    position: absolute;
    left: -40px;
    top: 70px;
    width: 460px;
    height: 560px;
    border-radius: 50%;
    background: radial-gradient(ellipse at 45% 45%, var(--teal-soft) 0%, rgba(59,89,84,0.55) 55%, rgba(47,75,71,0) 72%);
  }
  .company-name {
    position: absolute;
    left: 0;
    right: 0;
    top: 330px;
    text-align: center;
    color: var(--white);
    font-weight: 400;
  }
  .company-name .name {
    display: block;
    font-size: 48px;
    line-height: 1;
    letter-spacing: 0;
  }
  .company-name .descriptor {
    display: block;
    margin-top: 10px;
    font-size: 15px;
    letter-spacing: 0.5px;
  }

  /* Back envelope */
  .envelope-back {
    position: absolute;
    left: 640px;
    top: 300px;
    width: 450px;
    height: 590px;
    background: linear-gradient(160deg, var(--paper) 0%, var(--paper-shade) 100%);
    overflow: hidden;
    box-shadow: 0 6px 18px rgba(0,0,0,0.18);
  }
  .envelope-back .flap {
    position: absolute;
    left: 0;
    top: 0;
    width: 450px;
    height: 64px;
  }
  .envelope-back .globe-area {
    position: absolute;
    left: 70px;
    top: 30px;
    width: 340px;
    height: 400px;
    border-radius: 50%;
    background: radial-gradient(ellipse at 50% 45%, #dcdedd 0%, rgba(220,222,221,0.6) 55%, rgba(233,234,234,0) 72%);
  }
  .contact {
    position: absolute;
    left: 24px;
    bottom: 44px;
    font-size: 7.5px;
    line-height: 11px;
    color: var(--ink-muted);
    list-style: none;
  }
  .contact .gap { margin-top: 5px; }
  .base-band {
    position: absolute;
    left: 0;
    right: 0;
    bottom: 0;
    height: 12px;
    background: var(--teal-deep);
    border-top: 2px solid var(--gold-line);
  }
</style>
</head>
<body>
<main class="stationery">

  <section class="envelope-front">
    <div class="globe-area" role="img" aria-label="Faint world globe showing the Americas"></div>
    <h1 class="company-name">
      <span class="name">Virtal</span>
      <span class="descriptor">Soluções Ambientais</span>
    </h1>
  </section>

  <section class="envelope-back">
    <div class="globe-area" role="img" aria-label="Faint world globe showing the Americas"></div>
    <svg class="flap" viewBox="0 0 450 64" aria-hidden="true">
      <polygon points="0,0 450,0 410,64 40,64" fill="var(--teal-deep)"/>
    </svg>
    <ul class="contact">
      <li>contato@virtal.com.br</li>
      <li>+55 11 4000-1000</li>
      <li class="gap">Rua das Palmeiras, 120 - sala 45</li>
      <li>01234-000 São Paulo - SP</li>
      <li>+55 11 4000-1001</li>
    </ul>
    <div class="base-band"></div>
  </section>

</main>
</body>
</html>
```